Journeys With Marcella Business Cards

I need a business card design for my upscale Travel Agency.
Attached you can find my logo.
I would like to include the following:
- Name
- Title
- Phone Number
- Email
- Website
- and then something like: Follow us: JourneysWithMarcella (and then social media icons in color).
The logo should be in the front and then also the back.
I am also attaching a design that I liked (mostly for the layout) but open to any suggestions
Industry/Entity Type
Travel Agent
Contact Information for Business Card
Name: Marcella Dorn
Title: Travel Designer / Owner
Phone: 415-927-3308
Email: marcella@journeyswithmarcella-example.com
Website: www.JourneysWithMarcella-example.com
Social Media Handles for FB,IG, Twitter: JourneysWithMarcella
Colors
Designer to choose colors to be used in the design.
Look and feel

```html
<!DOCTYPE html>
<html lang="en">
<head>
<meta charset="utf-8">
<title>Journeys With Marcella – Business Card</title>
<link href="https://fonts.googleapis.com/css2?family=Roboto:wght@400;500&display=swap" rel="stylesheet">
<style>
  :root {
    --orange: #f3a95c;
    --ink: #1c1c1c;
    --white: #ffffff;
    --backdrop: #808080;
  }
  html, body {
    margin: 0;
    padding: 0;
    width: 1200px;
    height: 1020px;
    overflow: hidden;
    background: var(--backdrop);
    font-family: "Roboto", Arial, sans-serif;
  }
  .canvas {
    position: relative;
    width: 1200px;
    height: 1020px;
  }
  .card {
    position: absolute;
    left: 272px;
    width: 656px;
    height: 376px;
    border-radius: 23px;
    overflow: hidden;
  }
  .card--front { top: 88px; background: var(--white); }
  .card--back  { top: 514px; background: var(--orange); }

  .brand {
    position: absolute;
    display: flex;
    align-items: center;
  }
  .brand__square {
    display: block;
    flex: none;
  }
  .brand__name {
    font-weight: 500;
    letter-spacing: 0.2px;
  }
  .card--front .brand {
    left: 36px;
    top: 166px;
    gap: 10px;
  }
  .card--front .brand__square {
    width: 30px; height: 30px; background: var(--orange);
  }
  .card--front .brand__name {
    color: var(--orange);
    font-size: 20px;
    line-height: 1.15;
    width: 140px;
  }
  .card--back .brand {
    left: 50%;
    top: 170px;
    transform: translateX(-50%);
    gap: 16px;
    white-space: nowrap;
  }
  .card--back .brand__square {
    width: 42px; height: 42px; background: var(--white);
  }
  .card--back .brand__name {
    color: var(--white);
    font-size: 33px;
  }

  .divider {
    position: absolute;
    left: 226px;
    width: 2px;
    background: var(--orange);
  }
  .divider--name { top: 98px; height: 44px; }
  .divider--contact { top: 164px; height: 114px; }

  .person {
    position: absolute;
    left: 242px;
    top: 92px;
  }
  .person__name {
    margin: 0;
    font-size: 23px;
    font-weight: 500;
    color: var(--orange);
    line-height: 1.1;
  }
  .person__title {
    margin: 3px 0 0;
    font-size: 16px;
    font-weight: 400;
    color: var(--ink);
  }

  .contact {
    position: absolute;
    left: 242px;
    top: 160px;
    margin: 0;
    padding: 0;
    list-style: none;
  }
  .contact__item {
    display: flex;
    align-items: center;
    height: 24px;
    font-size: 16px;
    color: var(--ink);
    white-space: nowrap;
  }
  .contact__icon {
    width: 14px;
    height: 14px;
    margin-right: 11px;
    flex: none;
  }
  .social {
    display: flex;
    gap: 6px;
    margin-left: 10px;
  }
  .social__dot {
    width: 14px;
    height: 14px;
    border-radius: 50%;
    background: var(--orange);
  }
</style>
</head>
<body>
<main class="canvas">
  <section class="card card--front" aria-label="Business card front">
    <div class="brand">
      <span class="brand__square"></span>
      <span class="brand__name">Journeys With Marcella</span>
    </div>

    <span class="divider divider--name"></span>
    <div class="person">
      <h1 class="person__name">Marcella Dorn</h1>
      <p class="person__title">Travel Designer / Owner</p>
    </div>

    <span class="divider divider--contact"></span>
    <ul class="contact">
      <li class="contact__item">
        <svg class="contact__icon" viewBox="0 0 16 16" aria-hidden="true">
          <rect x="4" y="1" width="8" height="14" rx="1.5" fill="none" stroke="var(--orange)" stroke-width="1.6"/>
          <circle cx="8" cy="12.3" r="0.9" fill="var(--orange)"/>
        </svg>
        (415) 927-3308
      </li>
      <li class="contact__item">
        <svg class="contact__icon" viewBox="0 0 16 16" aria-hidden="true">
          <path d="M3.5 1.5l2.5 0 1 3.5-1.6 1.2c.8 1.8 2.2 3.2 4 4l1.2-1.6 3.5 1v2.5c0 .8-.7 1.4-1.5 1.4C6.9 13.5 2.5 9.1 2 3c0-.8.7-1.5 1.5-1.5z" fill="var(--orange)"/>
        </svg>
        (800) 555-0142
      </li>
      <li class="contact__item">
        <svg class="contact__icon" viewBox="0 0 16 16" aria-hidden="true">
          <rect x="1" y="3" width="14" height="10" fill="var(--orange)"/>
          <path d="M1 3l7 6 7-6" fill="none" stroke="var(--white)" stroke-width="1.2"/>
        </svg>
        marcella@journeyswithmarcella-example.com
      </li>
      <li class="contact__item">
        <svg class="contact__icon" viewBox="0 0 16 16" aria-hidden="true">
          <circle cx="8" cy="8" r="7" fill="var(--orange)"/>
          <path d="M1 8h14M8 1c-2.5 2.5-2.5 11.5 0 14M8 1c2.5 2.5 2.5 11.5 0 14" fill="none" stroke="var(--white)" stroke-width="0.9"/>
        </svg>
        www.JourneysWithMarcella-example.com
      </li>
      <li class="contact__item">
        <svg class="contact__icon" viewBox="0 0 16 16" aria-hidden="true">
          <circle cx="4" cy="8" r="2.2" fill="var(--orange)"/>
          <circle cx="12" cy="3.5" r="2.2" fill="var(--orange)"/>
          <circle cx="12" cy="12.5" r="2.2" fill="var(--orange)"/>
          <path d="M4 8l8-4.5M4 8l8 4.5" stroke="var(--orange)" stroke-width="1.3"/>
        </svg>
        Follow us: JourneysWithMarcella
        <span class="social" aria-label="Social media links">
          <span class="social__dot"></span>
          <span class="social__dot"></span>
          <span class="social__dot"></span>
        </span>
      </li>
    </ul>
  </section>

  <section class="card card--back" aria-label="Business card back">
    <div class="brand">
      <span class="brand__square"></span>
      <span class="brand__name">Journeys With Marcella</span>
    </div>
  </section>
</main>
</body>
</html>
```